new Ridgeway Bug Shield Flyer 8.5"x11"

We need a new flyer for our pest control company. We need it to be themed like our truck wrap. We have also attached is our old flyer.
The Best Defense is a Great Offense. Our Bug Guns are Locked, Loaded and Ready for action!
Don't be caught defenseless, Call Ridgeway Bug Shield today!!
"The Solution to your bug pollution"
www.ridgewaybugshield.com
352-481-6037

add a 10% off coupon code for existing Ridgeway Home Inspections customers

Target Market(s)

Home owners

Industry/Entity Type

Pest Control

Requirements
Must have
• our theme like our truck wrap

```html
<!DOCTYPE html>
<html lang="en">
<head>
<meta charset="utf-8">
<title>Ridgeway Bug Shield Flyer</title>
<link rel="stylesheet" href="https://fonts.googleapis.com/css2?family=Lato:wght@400;700;900&family=Anton&family=Arimo:wght@700&display=swap">
<style>
  :root {
    --red: #c0332b;
    --blue: #24479a;
    --ink: #2b2b2b;
    --coupon: #463f3b;
    --paper: #ecebe7;
    --camo: #c9ccae;
    --stage: #5a5a5a;
  }
  * { box-sizing: border-box; margin: 0; padding: 0; }
  html, body { width: 1200px; height: 1200px; overflow: hidden; }
  body { background: var(--stage); position: relative; font-family: 'Lato', sans-serif; }

  .flyer {
    position: absolute; left: 193px; top: 30px; width: 814px; height: 1140px;
    overflow: hidden; color: var(--ink);
    background:
      radial-gradient(ellipse 260px 180px at 60px 60px, rgba(180,185,140,.55), transparent 70%),
      radial-gradient(ellipse 220px 160px at 780px 300px, rgba(180,185,140,.45), transparent 70%),
      radial-gradient(ellipse 240px 170px at 40px 1060px, rgba(180,185,140,.6), transparent 70%),
      radial-gradient(ellipse 300px 200px at 420px 1120px, rgba(180,185,140,.45), transparent 70%),
      radial-gradient(ellipse 200px 140px at 150px 700px, rgba(200,200,190,.5), transparent 70%),
      var(--paper);
  }
  .shapes { position: absolute; inset: 0; width: 100%; height: 100%; }

  .brand { position: absolute; left: 31px; top: 90px; display: flex; align-items: center; gap: 10px;
    font-weight: 900; font-size: 26px; color: var(--ink); }
  .brand-dot { width: 22px; height: 22px; border-radius: 50%; background: var(--red); }

  .contact { position: absolute; left: 448px; top: 70px; }
  .contact-row { display: flex; align-items: center; gap: 12px; font-weight: 700; white-space: nowrap; }
  .contact-row svg { width: 28px; height: 28px; fill: var(--blue); }
  .phone { font-size: 30px; }
  .web { font-size: 21px; margin-top: 14px; }

  .center { position: absolute; left: 0; width: 100%; text-align: center; white-space: nowrap; }
  .lead { top: 248px; font-size: 43px; }
  .headline { top: 300px; font-family: 'Anton', sans-serif; font-size: 64px; font-weight: 400; color: var(--red); letter-spacing: 1px; }
  .today { position: absolute; left: 265px; top: 400px; width: 283px; height: 75px; background: var(--blue);
    color: #fff; font-family: 'Arimo', sans-serif; font-size: 64px; line-height: 75px; text-align: center; }
  .solution { top: 495px; font-size: 33px; }
  .solution b { color: var(--red); font-weight: 700; }
  .best { top: 550px; font-size: 28px; }
  .offense { top: 592px; font-size: 43px; font-weight: 700; color: var(--red); }

  .action { position: absolute; left: 54px; top: 698px; white-space: nowrap; }
  .action .locked { font-size: 37px; }
  .action .loaded { font-size: 31px; font-weight: 700; color: var(--red); }
  .action .go { font-family: 'Anton', sans-serif; font-size: 61px; color: var(--blue); letter-spacing: 2px; line-height: 1.2; }

  .coupon { position: absolute; left: 35px; top: 908px; width: 391px; height: 196px; }
  .coupon svg { position: absolute; inset: 0; }
  .coupon-text { position: absolute; inset: 0; display: flex; flex-direction: column; align-items: center; justify-content: center; color: #fff; text-align: center; white-space: nowrap; }
  .coupon-off { font-family: 'Anton', sans-serif; font-size: 56px; line-height: 1.1; color: var(--red); display: flex; align-items: center; gap: 12px; }
  .coupon-stars { font-family: 'Lato', sans-serif; font-size: 18px; color: #fff; letter-spacing: 3px; }
  .coupon-note { font-size: 18px; margin-top: 14px; }

  .mascot { position: absolute; left: 627px; top: 761px; width: 170px; height: 210px; border-radius: 8px;
    background: radial-gradient(ellipse at 50% 48%, #a9724a, #7a4a2c 55%, rgba(243,242,240,0) 78%); }
</style>
</head>
<body>
<main class="flyer">
  <svg class="shapes" viewBox="0 0 880 1232" preserveAspectRatio="none" aria-hidden="true">
    <polygon points="880,564 880,754 784,659" fill="var(--red)"/>
    <polygon points="752,666 1032,946 752,1226 472,946" fill="var(--red)"/>
    <polygon points="780,642 1060,922 780,1202 500,922" fill="var(--blue)"/>
    <polygon points="766,700 1002,936 766,1172 530,936" fill="var(--red)"/>
    <polygon points="770,716 990,936 770,1156 550,936" fill="#f3f2f0"/>
    <polygon points="559,1232 654,1144 744,1232" fill="var(--blue)"/>
  </svg>

  <div class="brand"><span class="brand-dot"></span>Ridgeway Bug Shield</div>

  <div class="contact">
    <div class="contact-row phone">
      <svg viewBox="0 0 24 24"><path d="M6.6 10.8a15 15 0 0 0 6.6 6.6l2.2-2.2a1 1 0 0 1 1-.25 11.4 11.4 0 0 0 3.6.57 1 1 0 0 1 1 1V20a1 1 0 0 1-1 1A17 17 0 0 1 3 4a1 1 0 0 1 1-1h3.5a1 1 0 0 1 1 1c0 1.25.2 2.45.57 3.57a1 1 0 0 1-.25 1z"/></svg>
      352-481-6037
    </div>
    <div class="contact-row web">
      <svg viewBox="0 0 24 24"><path d="M12 2a10 10 0 1 0 0 20 10 10 0 0 0 0-20zm6.9 6h-3a15.6 15.6 0 0 0-1.4-3.6A8 8 0 0 1 18.9 8zM12 4c.8 1.2 1.5 2.5 1.9 4h-3.8c.4-1.5 1.1-2.8 1.9-4zM4.3 14a8 8 0 0 1 0-4h3.4a16 16 0 0 0 0 4zm.8 2h3a15.6 15.6 0 0 0 1.4 3.6A8 8 0 0 1 5.1 16zm3-8h-3a8 8 0 0 1 4.4-3.6A15.6 15.6 0 0 0 8.1 8zM12 20c-.8-1.2-1.5-2.5-1.9-4h3.8c-.4 1.5-1.1 2.8-1.9 4zm2.3-6H9.7a14.6 14.6 0 0 1 0-4h4.6a14.6 14.6 0 0 1 0 4zm.2 5.6a15.6 15.6 0 0 0 1.4-3.6h3a8 8 0 0 1-4.4 3.6zm1.8-5.6a16 16 0 0 0 0-4h3.4a8 8 0 0 1 0 4z"/></svg>
      www.ridgewaybugshield.com
    </div>
  </div>

  <p class="center lead">Don't be caught defenseless</p>
  <h1 class="center headline">CALL RIDGEWAY BUG SHIELD</h1>
  <div class="today">TODAY</div>
  <p class="center solution">The Solution to your <b>BUG POLLUTION</b></p>
  <p class="center best">The Best Defense is a</p>
  <p class="center offense">GREAT OFFENSE</p>

  <div class="action">
    <p class="locked">Our Bug Guns are Locked</p>
    <p class="loaded">Loaded and Ready</p>
    <p class="go">FOR ACTION</p>
  </div>

  <div class="coupon">
    <svg viewBox="0 0 391 196" width="391" height="196" aria-hidden="true">
      <path d="M0 10 L10 0 L280 0 A32 32 0 0 0 344 0 L381 0 L391 10 L384 30 L391 50 L384 70 L391 90 L384 110 L391 130 L384 150 L391 170 L381 196 L344 196 A32 32 0 0 0 280 196 L10 196 L0 186 L7 166 L0 146 L7 126 L0 106 L7 86 L0 66 L7 46 L0 26 Z" fill="var(--coupon)"/>
    </svg>
    <div class="coupon-text">
      <p class="coupon-off"><span class="coupon-stars">★★★</span>10% OFF<span class="coupon-stars">★★★</span></p>
      <p class="coupon-note"><b>Ridgeway</b> Home Inspections customers</p>
    </div>
  </div>

  <div class="mascot" role="img" aria-label="Cartoon cockroach waving a white flag inside a red targeting crosshair"></div>
</main>
</body>
</html>
```